Tea Shop - Drinks Menu - Vertical TV screen

Need a drinks menu design for a tea shop based in The Netherlands. Called BrewLoom.
Currently we are trying to attract more customers for our Cup4Walk and the idea came up to place 3 TV screen vertically in order to use 2 for the menu.
Website: http://brewloom-zuidplein.example.nl/
Posible colour themes -
- Light green (same green as logo)
- Light brown
Dimensions of the screen -
- 40inch
- 905 mm Height
- 207 mm Width
Resolution of the menu must be 1920x1080 BUT VERTICAL
Needs to contain the following -
- Hot Cup4Walk
- BLACK
- Gentle Baron Slate
- Sweet Papaya Hug
- Plummy Orchard
- Spicy Chai
- Black Assam
- Duchess of Hillcrest
- Smokey Lapsang Suochong
- ( and many more teas, so leave space for aditional 5+)
- GREEN
- Sencha Lime-Ginger
- Sencha Forest Berries
- Sencha Orange Choco
- Happy Lotus
- Bancha
- Classic Gunpowder
- (space for aditional 4+)
- OOLONG
- Bullet Oolong
- Milky Oolong
- WHITE
- Bai Mu Tan
- HERBAL
- BrewLoom's Wish
- Refreshing Lindenbloom
- Pure Ginger
- Moon Blend
- Nana Mint
- Basil Strawberry
- FRUIT TEA
- Fruity Almond
- Tutti Fruity
- Melon Hug
- Spicy Pear
- Alpine Quince
- (space for aditional 2+)
- LATTÉ
- Spiced Chai
- Green Chai
- Vanille Chai
- Matcha
- Fresh Mint tea
- Iced Tea
- Peach
- Raspberry
- Lemon
- Mango
Divide this menu over 2 TV screens with the mentioned dimensions and use the font provided in the uploaded files (not mandatory if you think you have a bette idea).
Simple
Needs to attract people
Easy to adjust
Idea's are always welcome and appreciated
LOGO LINK : http://img4.picvault.example/7kq9zd3.png
(image too big to upload on here, sorry)
people whom drink TEA
Tv

```html
<!DOCTYPE html>
<html lang="en">
<head>
<meta charset="utf-8">
<title>BrewLoom – Drinks Menu Screens</title>
<link rel="stylesheet" href="https://fonts.googleapis.com/css2?family=Ubuntu:wght@400;500&display=swap">
<style>
  :root {
    --brown: #7a6b5d;
    --green: #bedb5f;
    --green-deep: #1f6a12;
    --green-mid: #6fb52a;
    --ink: #1f1f1f;
    --paper: #ffffff;
    --canvas: #f4f4f2;
    --logo: #5b4b3f;
  }
  * { box-sizing: border-box; margin: 0; padding: 0; }
  html, body { width: 1200px; height: 1030px; overflow: hidden; }
  body {
    background: var(--canvas);
    font-family: "Ubuntu", sans-serif;
    position: relative;
  }
  .screen {
    position: absolute;
    top: 26px;
    width: 548px;
    height: 974px;
    background: var(--paper);
    box-shadow: 0 1px 4px rgba(0,0,0,.25);
    display: flex;
    flex-direction: column;
    overflow: hidden;
  }
  .screen--left { left: 40px; }
  .screen--right { left: 612px; }

  .hero {
    height: 106px;
    background: linear-gradient(90deg, #1d2230 0%, #2b3142 30%, #a77b4d 48%, #d8c3a0 60%, #8c3b2e 72%, #b2262a 80%, #e9e2d4 92%, #f3f0ea 100%);
  }
  .band {
    height: 18px;
    background: linear-gradient(180deg, var(--green-deep) 0 3px, var(--green-mid) 3px 11px, #9ccf45 11px 14px, var(--green-deep) 14px 18px);
  }
  .band--thin {
    height: 12px;
    background: linear-gradient(180deg, var(--green-deep) 0 3px, var(--green-mid) 3px 9px, var(--green-deep) 9px 12px);
  }

  .section {
    display: grid;
    grid-template-columns: 220px 108px 220px;
    font-size: 15px;
    line-height: 25.4px;
  }
  .section--brown { background: var(--brown); color: #fff; }
  .section--green { background: var(--green); color: var(--ink); }

  .list { list-style: none; }
  .list--start { padding-left: 29px; }
  .list--end { padding-right: 28px; text-align: right; white-space: nowrap; }
  .list .heading { text-transform: uppercase; }

  .photo-column {
    display: flex;
    flex-direction: column;
    border-left: 2px solid var(--paper);
    border-right: 2px solid var(--paper);
    gap: 2px;
    background: var(--paper);
  }
  .photo-column .photo { flex: 1; }

  .footer {
    flex: 1;
    display: grid;
    grid-template-columns: 280px 1fr;
  }
  .footer .photo { height: 100%; }
  .brand {
    display: flex;
    align-items: center;
    justify-content: center;
    font-size: 50px;
    font-weight: 400;
    color: var(--logo);
    letter-spacing: -0.5px;
  }
</style>
</head>
<body>

<!-- Screen one -->
<section class="screen screen--left">
  <div class="hero" role="img" aria-label="Customer pointing at a shelf of tea tins in the shop"></div>
  <div class="band"></div>

  <div class="section section--brown" style="height:257px">
    <ul class="list list--start" style="padding-top:40px">
      <li class="heading">Herbal</li>
      <li>BrewLoom's Wish</li>
      <li>Refreshing Lindenbloom</li>
      <li>Pure Ginger</li>
      <li>Moon Blend</li>
      <li>Nana Mint</li>
    </ul>
    <div class="photo-column">
      <div class="photo" role="img" aria-label="Takeaway tea cups on the counter" style="background:linear-gradient(180deg,#eae6df,#c9a77c 60%,#e5ddd2)"></div>
      <div class="photo" role="img" aria-label="Bags of loose herbal tea" style="background:linear-gradient(180deg,#4f6a2a,#c9c0a3 55%,#8a7a5c)"></div>
    </div>
    <ul class="list list--end" style="padding-top:40px">
      <li>Basil Strawberry</li>
      <li>=</li>
      <li>=</li>
      <li>=</li>
      <li>=</li>
    </ul>
  </div>

  <div class="section section--green" style="height:192px">
    <ul class="list list--start" style="padding-top:61px">
      <li class="heading">Fruit Tea</li>
      <li>Fruity Almond</li>
      <li>Tutti Fruity</li>
      <li>Melon Hug</li>
    </ul>
    <div class="photo-column">
      <div class="photo" style="flex:0 0 57px;background:linear-gradient(180deg,#d8d8d4,#7c7c78 50%,#dcdcd8)" role="img" aria-label="Row of tea tins on a shelf"></div>
      <div class="photo" role="img" aria-label="Packaged teas displayed on glass shelves" style="background:linear-gradient(180deg,#c98f4e,#5a8a3a 40%,#2c2f3a 75%,#d7d3cb)"></div>
    </div>
    <ul class="list list--end" style="padding-top:64px">
      <li>Spicy Pear</li>
      <li>Alpine Quince</li>
      <li>=</li>
      <li>-</li>
    </ul>
  </div>

  <div class="section section--brown" style="height:228px">
    <ul class="list list--start" style="padding-top:48px;padding-left:33px">
      <li class="heading">Latté</li>
      <li>Spiced Chai</li>
      <li>Green Chai</li>
      <li>Vanille Chai</li>
      <li>Matcha</li>
    </ul>
    <div class="photo-column">
      <div class="photo" role="img" aria-label="Iced tea in a takeaway cup with a straw" style="background:linear-gradient(180deg,#eeeae4,#b9d7e0 35%,#3a2a3c 60%,#c09464 85%,#f0ece6)"></div>
    </div>
    <ul class="list list--end" style="padding-top:46px">
      <li>Fresh Mint tea</li>
      <li>Iced Tea</li>
      <li>Peach</li>
      <li>Raspberry</li>
      <li>Lemon</li>
      <li>Mango</li>
    </ul>
  </div>

  <div class="band--thin"></div>
  <div class="footer">
    <div class="photo" role="img" aria-label="Scoop pouring loose tea into a paper bag" style="background:linear-gradient(120deg,#f0c070,#d9953a 45%,#b06a22 75%,#f2c88a)"></div>
    <div class="brand">BrewLoom</div>
  </div>
</section>

<!-- Screen two -->
<section class="screen screen--right">
  <div class="hero" role="img" aria-label="Customer pointing at a shelf of tea tins in the shop"></div>
  <div class="band"></div>

  <div class="section section--green" style="height:258px">
    <ul class="list list--start" style="padding-top:40px">
      <li>Hot Cup4Walk</li>
      <li class="heading">Black</li>
      <li>Gentle Baron Slate</li>
      <li>Sweet Papaya Hug</li>
      <li>Plummy Orchard</li>
      <li>Spicy Chai</li>
      <li>Black Assam</li>
    </ul>
    <div class="photo-column">
      <div class="photo" role="img" aria-label="Scoop of loose tea over a green paper bag" style="background:linear-gradient(180deg,#7a9a55,#5c4a3c 40%,#1f5a24 70%,#6a5a4a)"></div>
    </div>
    <ul class="list list--end" style="padding-top:40px">
      <li>Duchess of Hillcrest</li>
      <li>Smokey Lapsang Suochong</li>
      <li>=</li>
      <li>=</li>
      <li>=</li>
      <li>=</li>
      <li>=</li>
    </ul>
  </div>

  <div class="section section--brown" style="height:246px">
    <ul class="list list--start" style="padding-top:50px">
      <li class="heading">Green</li>
      <li>Sencha Lime-Ginger</li>
      <li>Sencha Forest Berries</li>
      <li>Sencha Orange Choco</li>
      <li>Happy Lotus</li>
      <li>Bancha</li>
    </ul>
    <div class="photo-column">
      <div class="photo" style="flex:0 0 110px;background:radial-gradient(circle at 50% 55%,#a0522d,#6a4a2a 45%,#9c9c98 75%,#dcdcd8)" role="img" aria-label="Tin filled with fruity loose tea"></div>
      <div class="photo" role="img" aria-label="Labelled green tea bags" style="background:linear-gradient(180deg,#2f7a2a,#e8e8e4 45%,#3c8a30)"></div>
    </div>
    <ul class="list list--end" style="padding-top:50px">
      <li>Classic Gunpowder</li>
      <li>=</li>
      <li>=</li>
      <li>=</li>
      <li>=</li>
    </ul>
  </div>

  <div class="section section--green" style="height:172px">
    <ul class="list list--start" style="padding-top:50px">
      <li class="heading">Oolong</li>
      <li>Bullet Oolong</li>
      <li>Milky Oolong</li>
    </ul>
    <div class="photo-column">
      <div class="photo" role="img" aria-label="Matcha latte in a takeaway cup" style="background:linear-gradient(180deg,#e4ead0,#cfe0a0 25%,#f0ece4 45%,#c6925c 75%,#e8e0d4)"></div>
    </div>
    <ul class="list list--end" style="padding-top:50px">
      <li class="heading">White</li>
      <li>Bai Mu Tan</li>
    </ul>
  </div>

  <div class="band--thin"></div>
  <div class="footer">
    <div class="photo" role="img" aria-label="Metal scoop with loose tea above a green bag" style="background:linear-gradient(120deg,#d9a080,#8a6a4a 35%,#c8c0b4 55%,#2f6a24 80%,#5a8a3a)"></div>
    <div class="brand">BrewLoom</div>
  </div>
</section>

</body>
</html>
```